Car dent,ding,crease removal. This will be for the Automotive industry, bodywork repair.

I need a double sided business card designing.

Company name is Ding Mender and we remove small car park dents creases and dings.

The card should have sleek car design/outline on it.

The wording Paintless Dent Removal to be on the card.

The background colours used should include Royal blue, black, and a hint of red.

Need a sleek modern look, clean lines.

I really don't want designers going to my website and just copying the car design, I want something new!

Reason: I've put a guaranteed payment on the design now.

Automotive

Must have
• Paintless Dent Removal
Ding Mender
Gareth Holloway
enquiries@dingmender.co.uk
07912364580
Covering, Chester, North Wales and the Wirral
Free quotes available
www.dingmender.co.uk

```html
<!DOCTYPE html>
<html lang="en">
<head>
<meta charset="utf-8">
<title>Ding Mender – Business Card</title>
<link rel="stylesheet" href="https://fonts.googleapis.com/css2?family=Roboto:wght@400;500;700&display=swap">
<style>
  :root {
    --royal-blue: #2443a6;
    --royal-blue-light: #2e52bd;
    --royal-blue-deep: #1a3189;
    --signal-red: #d12b2b;
    --paper-white: #ffffff;
    --logo-blue: #2a4ba8;
    --soft-white: #dfe6f7;
    --stage-black: #121216;
  }
  * { box-sizing: border-box; margin: 0; padding: 0; }
  html, body {
    width: 1200px;
    height: 800px;
    overflow: hidden;
    background: var(--stage-black);
    font-family: "Roboto", Arial, sans-serif;
  }
  .card-spread {
    position: relative;
    width: 1200px;
    height: 800px;
    display: flex;
    align-items: center;
    justify-content: center;
    gap: 60px;
  }
  .card {
    position: relative;
    width: 520px;
    height: 300px;
    overflow: hidden;
    border-radius: 4px;
    box-shadow: 0 14px 34px rgba(0,0,0,0.6);
  }
  .card-art {
    position: absolute;
    inset: 0;
    width: 100%;
    height: 100%;
  }
  .brand-mark {
    display: inline-block;
    flex: none;
    border-radius: 50%;
  }

  /* Front */
  .card--front {
    background: radial-gradient(ellipse at 45% 42%, var(--royal-blue-light) 0%, var(--royal-blue) 45%, var(--royal-blue-deep) 100%);
    color: var(--paper-white);
  }
  .front-brand {
    position: absolute;
    left: 0;
    right: 0;
    top: 84px;
    text-align: center;
  }
  .front-brand .brand-row {
    display: flex;
    align-items: center;
    justify-content: center;
    gap: 14px;
  }
  .front-brand .brand-mark {
    width: 24px;
    height: 24px;
    background: var(--paper-white);
  }
  .front-brand .brand-name {
    font-size: 54px;
    font-weight: 700;
    line-height: 1;
    color: var(--paper-white);
  }
  .front-brand .tagline {
    margin-top: 10px;
    font-size: 25px;
    font-weight: 400;
    color: var(--soft-white);
  }
  .coverage {
    position: absolute;
    left: 0;
    right: 0;
    top: 222px;
    text-align: center;
    font-size: 14px;
    color: var(--soft-white);
  }

  /* Back */
  .card--back { background: var(--paper-white); }
  .back-brand {
    position: absolute;
    left: 30px;
    top: 32px;
  }
  .back-brand .brand-row {
    display: flex;
    align-items: center;
    gap: 9px;
  }
  .back-brand .brand-mark {
    width: 14px;
    height: 14px;
    background: var(--logo-blue);
  }
  .back-brand .brand-name {
    font-size: 34px;
    font-weight: 700;
    line-height: 1;
    color: var(--logo-blue);
  }
  .back-brand .tagline {
    margin-top: 5px;
    margin-left: 23px;
    font-size: 16px;
    color: var(--logo-blue);
  }
  .offer {
    position: absolute;
    left: 26px;
    top: 160px;
    font-size: 23px;
    font-weight: 700;
    line-height: 1.2;
    color: var(--paper-white);
    text-transform: uppercase;
  }
  .contact {
    position: absolute;
    right: 26px;
    top: 100px;
    text-align: right;
    color: var(--paper-white);
  }
  .contact .person {
    font-size: 17px;
    font-weight: 700;
    text-transform: uppercase;
    letter-spacing: 0.5px;
    margin-bottom: 32px;
  }
  .contact .line {
    font-size: 14px;
    line-height: 1.75;
  }
  .contact .web {
    margin-top: 12px;
    font-size: 15px;
    font-weight: 700;
  }
</style>
</head>
<body>
  <main class="card-spread">
    <section class="card card--front" aria-label="Business card front">
      <div class="front-brand">
        <div class="brand-row">
          <span class="brand-mark" aria-hidden="true"></span>
          <span class="brand-name">Ding Mender</span>
        </div>
        <div class="tagline">Paintless Dent Removal</div>
      </div>
      <p class="coverage">Covering, Chester, North Wales and the Wirral</p>
    </section>

    <section class="card card--back" aria-label="Business card back">
      <svg class="card-art" viewBox="0 0 520 300" aria-hidden="true">
        <polygon points="385,0 520,0 520,300 175,300" fill="var(--royal-blue)"/>
        <polygon points="0,140 279,140 209,240 0,240" fill="var(--signal-red)"/>
      </svg>
      <div class="back-brand">
        <div class="brand-row">
          <span class="brand-mark" aria-hidden="true"></span>
          <span class="brand-name">Ding Mender</span>
        </div>
        <div class="tagline">Paintless Dent Removal</div>
      </div>
      <p class="offer">Free quotes<br>available</p>
      <div class="contact">
        <p class="person">Gareth Holloway</p>
        <p class="line">enquiries@dingmender.co.uk</p>
        <p class="line">07912364580</p>
        <p class="web">www.dingmender.co.uk</p>
      </div>
    </section>
  </main>
</body>
</html>
```